The Merry Hound - Dog Training Business Card Design

I need a business card design for a new dog training company based in Cronulla NSW called The Merry Hound. I run puppy pre school classes, adult dog classes and do one on one training in the person's home.
I have studied for 2 years and use positive reinforcement training methods based on how dogs learn. I believe in communicating with our dogs what we want them to do rather than punish them for behaviours we don't like. I would like to see designs that use the colours that are used in my logo (please see attached)
I would like a simple and classic looking design. I don't want cartoon images of dogs or any animal images or drawings on the card. I have created my logo with this mindset. I am open to the subtle use of a dog's tail, paws or paw print.

Target Market(s)

high end area which is why I want a classic looking design
adults aged 25 and over

Industry/Entity Type

Dog Training

Contact Information for Business Card

Miriam Caslett
ORBIS Trained Professional Dog Trainer
www.themerryhound-example.com.au
0499731628
miriam@themerryhound-example.com.au

Font styles to use
Sans Serif

Colors
ffffff
86cae6
757575

Requirements
Must have
• Logo - I am trying to attach my logo and colour palette but it won't allow me. I will contact the company and upload ASAP.
Should not have
• images of dogs or cartoon drawings

```html
<!DOCTYPE html>
<html lang="en">
<head>
<meta charset="utf-8">
<title>The Merry Hound – Business Card</title>
<link rel="stylesheet" href="https://fonts.googleapis.com/css2?family=Noto+Serif:wght@400;700&display=swap">
<style>
  :root {
    --white: #ffffff;
    --sky: #86cae6;
    --sky-deep: #5fb3d6;
    --grey: #757575;
    --ink: #1d1d1d;
    --backdrop: #e9e7e3;
  }
  * { box-sizing: border-box; margin: 0; padding: 0; }
  html, body {
    width: 1200px; height: 844px; overflow: hidden;
    background: var(--backdrop);
    font-family: "Noto Serif", Georgia, serif;
  }
  .sheet {
    position: relative; width: 1200px; height: 844px;
    display: flex; justify-content: center; align-items: center; gap: 80px;
  }
  .card {
    position: relative; width: 340px; height: 560px;
    border-radius: 22px;
    box-shadow: 0 6px 18px rgba(0,0,0,.18);
    overflow: hidden;
  }
  .card--front { background: var(--white); }
  .card--back {
    background: linear-gradient(160deg, var(--sky) 0%, #9fd6ee 45%, var(--sky-deep) 100%);
  }
  .brand {
    position: absolute; left: 0; right: 0;
    display: flex; align-items: center; justify-content: center; gap: 10px;
    font-weight: 700; font-size: 30px; color: var(--grey);
    letter-spacing: .5px;
  }
  .card--front .brand { top: 150px; }
  .card--back .brand { top: 250px; color: var(--white); }
  .brand__dot {
    width: 14px; height: 14px; border-radius: 50%;
    background: var(--sky);
  }
  .card--back .brand__dot { background: var(--white); }
  .details {
    position: absolute; left: 30px; right: 30px; top: 290px;
    text-align: center;
  }
  .details__name {
    font-weight: 700; font-size: 22px; letter-spacing: 1px;
    color: var(--ink); text-transform: uppercase;
  }
  .details__role {
    font-size: 15px; color: var(--grey); line-height: 1.4; margin-top: 6px;
  }
  .details__rule {
    border: 0; border-top: 1px dotted var(--grey);
    margin: 14px 0;
  }
  .details__phone {
    display: flex; align-items: center; justify-content: center; gap: 8px;
    font-size: 27px; color: var(--sky); letter-spacing: 1px;
  }
  .details__phone svg { width: 24px; height: 24px; }
  .details__line {
    font-size: 13.5px; color: var(--grey); line-height: 1.6;
  }
  .back__web {
    position: absolute; left: 0; right: 0; bottom: 40px;
    text-align: center; font-size: 14px; color: var(--grey);
  }
</style>
</head>
<body>
<main class="sheet">
  <section class="card card--front" aria-label="Business card front">
    <div class="brand"><span class="brand__name">The Merry Hound</span><span class="brand__dot"></span></div>
    <div class="details">
      <p class="details__name">Miriam Caslett</p>
      <p class="details__role">ORBIS Trained<br>Professional Dog Trainer</p>
      <hr class="details__rule">
      <p class="details__phone">
        <svg viewBox="0 0 24 24" aria-hidden="true"><path fill="#86cae6" d="M6.6 10.8a15.1 15.1 0 0 0 6.6 6.6l2.2-2.2c.3-.3.7-.4 1-.2 1.1.4 2.3.6 3.6.6.6 0 1 .4 1 1V20c0 .6-.4 1-1 1A17 17 0 0 1 3 4c0-.6.4-1 1-1h3.5c.6 0 1 .4 1 1 0 1.3.2 2.5.6 3.6.1.3 0 .7-.2 1z"/></svg>
        0499731628
      </p>
      <hr class="details__rule">
      <p class="details__line">miriam@themerryhound-example.com.au</p>
      <p class="details__line">www.themerryhound-example.com.au</p>
    </div>
  </section>
  <section class="card card--back" aria-label="Business card back">
    <div class="brand"><span class="brand__name">The Merry Hound</span><span class="brand__dot"></span></div>
    <p class="back__web">www.themerryhound-example.com.au</p>
  </section>
</main>
</body>
</html>
```